QTRW needs 2 complementary employee newsletter header designs - 1) VF News and 2) the Arc. We are reimagining VF News to be a fresh, engaging, talent forward internal newsletter that reflects the energy, growth and commitment to our people at QTRW. This evolved design should be modern, dynamic and cohesive with QTRW’s brand, reinforcing that our people are at the center of everything we do. The newsletter will deliver essential company updates, culture highlights, employee spotlights, event news and more – ensuring that the largest component of QTRW – Tax, Audit and Advisory teams – stay informed and connected. The design should embrace a balance of professionalism and warmth, capturing our culture beyond accounting and inspiring engagement, growth and connection.
VF News will complement the Arc, a newsletter that serves all of QTRW and the QTRW Family of Companies, while serving as a dedicated and elevated resource, central internal communication tool for the company, ensuring employees sees their role in our collective success.
The colors on the previous banner were dated – we are looking for modern, engaging colors.
We are looking to refresh that one as well as the VF News header that replaces the attached 5x5 header - please don't use colors similar to the purple and green on this header.

Target Market(s)

internal/employees

Industry/Entity Type

accounting and business consulting

Font styles to use
Sans Serif

Colors
0054AA
0677BA
7BADD7
CADEEF
E8F1F8
0094D4
00A9DD
6FCCEA
C7EBF8
E9F6FB
00AB8E
00BBA5
67D7C9
C6EFE9
E9F9F6

Requirements
Must have
• clean, crisp, and modern design, with QTRW logo, hex color 009add should be included in some manner
Nice to have
• see description
Should not have
• dated colors such as the attached 5x5 header, should not look AI generated

```html
<!DOCTYPE html>
<html lang="en">
<head>
<meta charset="utf-8">
<title>VF News Header</title>
<link href="https://fonts.googleapis.com/css2?family=Barlow:wght@500;600;700&display=swap" rel="stylesheet">
<style>
  :root {
    --brand-blue: #1ea6e0;
    --ink: #151515;
    --slate: #474b4f;
    --white: #ffffff;
    --wall-top: #f6f7f8;
    --wall-mid: #e9ebed;
    --wall-low: #d4d8dc;
    --desk: #4f5a64;
  }
  * { margin: 0; padding: 0; box-sizing: border-box; }
  html, body {
    width: 1200px;
    height: 400px;
    overflow: hidden;
    background: var(--white);
  }
  .header-banner {
    position: relative;
    width: 1200px;
    height: 400px;
    overflow: hidden;
    font-family: "Barlow", Arial, sans-serif;
  }
  .backdrop {
    position: absolute;
    inset: 0;
    background:
      linear-gradient(180deg, transparent 0%, transparent 80%, rgba(79,90,100,0.55) 88%, var(--desk) 100%),
      linear-gradient(180deg, var(--wall-top) 0%, var(--wall-mid) 55%, var(--wall-low) 82%);
  }
  .headline {
    position: absolute;
    left: 80px;
    top: 146px;
  }
  .headline-title {
    font-size: 46px;
    font-weight: 600;
    color: var(--brand-blue);
    line-height: 1;
    letter-spacing: 0.2px;
  }
  .headline-pillars {
    margin-top: 14px;
    font-size: 52px;
    font-weight: 600;
    color: var(--ink);
    line-height: 1;
    letter-spacing: 0.3px;
  }
  .service-grid {
    position: absolute;
    left: 0;
    top: 0;
    width: 1200px;
    height: 400px;
  }
  .cell { stroke: var(--white); stroke-width: 6; }
  .cell-blue { fill: var(--brand-blue); }
  .cell-slate { fill: var(--slate); }
  .cell-label {
    font-family: "Barlow", Arial, sans-serif;
    font-size: 23px;
    font-weight: 600;
    fill: var(--white);
    text-anchor: middle;
    dominant-baseline: middle;
  }
</style>
</head>
<body>
<div class="header-banner">
  <div class="backdrop" role="img" aria-label="Soft-focus photo of a pale concrete wall above a dark desk surface"></div>

  <div class="headline">
    <h1 class="headline-title">VF News:</h1>
    <p class="headline-pillars">People | Growth | Technology</p>
  </div>

  <svg class="service-grid" viewBox="0 0 1200 400" xmlns="http://www.w3.org/2000/svg">
    <defs>
      <path id="hex" d="M0,-78 L68,-39 L68,39 L0,78 L-68,39 L-68,-39 Z"/>
      <linearGradient id="tone-tower" x1="0" y1="0" x2="1" y2="1">
        <stop offset="0" stop-color="#9fb9d6"/>
        <stop offset="1" stop-color="#3d6a9c"/>
      </linearGradient>
      <linearGradient id="tone-strategy" x1="0" y1="0" x2="1" y2="1">
        <stop offset="0" stop-color="#cfc7bb"/>
        <stop offset="1" stop-color="#3a3835"/>
      </linearGradient>
      <linearGradient id="tone-data" x1="0" y1="0" x2="1" y2="1">
        <stop offset="0" stop-color="#2d6fc0"/>
        <stop offset="1" stop-color="#0c1f4a"/>
      </linearGradient>
      <linearGradient id="tone-office" x1="0" y1="0" x2="1" y2="1">
        <stop offset="0" stop-color="#e9e3da"/>
        <stop offset="1" stop-color="#d89a5c"/>
      </linearGradient>
    </defs>

    <g transform="translate(872,70)">
      <use href="#hex" class="cell cell-blue"/>
      <text class="cell-label">Audit</text>
    </g>
    <g transform="translate(1006,44)" role="img" aria-label="Photo of a glass office tower against the sky">
      <use href="#hex" class="cell" fill="url(#tone-tower)"/>
    </g>
    <g transform="translate(1140,70)">
      <use href="#hex" class="cell cell-slate"/>
      <text class="cell-label">Tax</text>
    </g>

    <g transform="translate(938,184)" role="img" aria-label="Photo of chess pieces on a board">
      <use href="#hex" class="cell" fill="url(#tone-strategy)"/>
    </g>
    <g transform="translate(1072,184)" role="img" aria-label="Abstract blue digital data visual">
      <use href="#hex" class="cell" fill="url(#tone-data)"/>
    </g>

    <g transform="translate(872,298)">
      <use href="#hex" class="cell cell-slate"/>
      <text class="cell-label">Advisory</text>
    </g>
    <g transform="translate(1006,330)" role="img" aria-label="Photo of a bright modern office interior">
      <use href="#hex" class="cell" fill="url(#tone-office)"/>
    </g>
    <g transform="translate(1140,298)">
      <use href="#hex" class="cell cell-blue"/>
      <text class="cell-label">Enterprise</text>
    </g>
  </svg>
</div>
</body>
</html>
```